Web design for Money Service Business (uncoded)

We need a very basic website with 5-6 pages. Home page, Services, Transfer(How to use our service), About us, Contact us, FAQ
Our company name is Meridale Exchange. We are a company that deals with currency exchange and international money transfer. We do cash exchange and international money transfers to bank accounts all over the world. We offer highly competitive exchange rates so usually attract customers who transfer money over $10,000. Our niche is with larger sums of money, the design needs to be professional and communicate trust, security and stability.

```html
<!DOCTYPE html>
<html lang="en">
<head>
<meta charset="utf-8">
<title>Meridale Exchange — International Money Transfer</title>
<link href="https://fonts.googleapis.com/css2?family=Questrial&family=Arimo:ital,wght@0,400;0,700;1,400&display=swap" rel="stylesheet">
<style>
  :root {
    --navy: #1f4e7a;
    --navy-deep: #0e3d6a;
    --blue-card: #1e5a8a;
    --blue-btn: #2a6496;
    --orange: #f7941d;
    --header-bg: #f6f6f6;
    --hero-bg: #eaf0f5;
    --strip-bg: #ececec;
    --card-bg: #efeeee;
    --text: #555555;
    --muted: #8a8a8a;
    --dark-btn: #454545;
    --white: #ffffff;
  }
  * { margin: 0; padding: 0; box-sizing: border-box; }
  html, body { width: 1200px; height: 1121px; overflow: hidden; }
  body { position: relative; background: var(--white); font-family: "Arimo", Arial, sans-serif; color: var(--text); }
  .abs { position: absolute; }

  .site-header { left: 0; top: 0; width: 1200px; height: 110px; background: var(--header-bg); }
  .brand { left: 204px; top: 30px; }
  .brand-name { font-family: "Questrial", sans-serif; font-size: 40px; line-height: 44px; color: var(--navy); letter-spacing: 0.5px; }
  .brand-tagline { font-family: "Questrial", sans-serif; font-size: 12.5px; letter-spacing: 3.6px; color: var(--navy); margin-top: 1px; }
  .social { top: 38px; width: 29px; height: 29px; border-radius: 50%; }
  .social-a { left: 919px; background: #3b5998; }
  .social-b { left: 951px; background: #3fa9e0; }
  .social-c { left: 984px; background: #cc2127; }

  .main-nav { left: 0; top: 110px; width: 1200px; height: 39px; background: var(--white); }
  .nav-item { top: 13px; font-size: 10px; color: #888; }
  .nav-item.is-active { color: var(--navy); }
  .nav-underline { left: 204px; top: -1px; width: 41px; height: 2px; background: var(--navy); }

  .hero { left: 0; top: 149px; width: 1200px; height: 302px; background: var(--hero-bg); }
  .hero-title { left: 204px; top: 80px; font-family: "Questrial", sans-serif; font-size: 22px; line-height: 25px; color: var(--navy); }
  .hero-sub { left: 204px; top: 146px; font-family: "Questrial", sans-serif; font-size: 17px; color: var(--orange); }
  .btn-learn { left: 204px; top: 186px; width: 82px; height: 26px; border-radius: 4px; background: var(--blue-btn); color: var(--white); font-size: 10px; line-height: 26px; text-align: center; }
  .hero-art { left: 460px; top: 8px; width: 566px; height: 294px; background: linear-gradient(90deg, rgba(215,70,60,0.55) 0%, rgba(80,120,200,0.7) 35%, #3f66c4 100%); border-radius: 2px; }

  .intro-strip { left: 204px; top: 479px; width: 820px; height: 73px; background: var(--strip-bg); }
  .strip-brand { left: 28px; top: 27px; font-family: "Questrial", sans-serif; font-size: 13px; color: #777; }
  .strip-text { left: 169px; top: 27px; width: 500px; font-size: 9.5px; line-height: 12px; color: #444; }
  .btn-strip { left: 685px; top: 24px; width: 110px; height: 31px; background: var(--dark-btn); color: var(--white); font-size: 10px; font-weight: 700; line-height: 31px; text-align: center; }

  .features { left: 204px; top: 576px; width: 820px; height: 226px; box-shadow: -6px 0 10px -6px rgba(0,0,0,0.35), 6px 0 10px -6px rgba(0,0,0,0.35); }
  .card { top: 4px; width: 256px; height: 218px; border: 1px solid #dcdcdc; background: #fafafa; }
  .card-media { left: 0; top: 0; width: 254px; height: 130px; background: #fafafa; }
  .card-media span { position: absolute; left: 50%; top: 50%; transform: translate(-50%, -50%); width: 120px; height: 80px; border-radius: 6px; }
  .card-body { left: 0; top: 130px; width: 254px; height: 86px; background: var(--card-bg); text-align: center; }
  .card-title { margin-top: 14px; font-family: "Questrial", sans-serif; font-size: 13.5px; color: var(--navy); }
  .card-text { margin: 8px auto 0; width: 215px; font-size: 8.5px; line-height: 12.5px; color: #666; }
  .card.is-featured .card-body { background: var(--blue-card); }
  .card.is-featured .card-title, .card.is-featured .card-text { color: var(--white); }

  .section-title { font-family: "Questrial", sans-serif; font-size: 13px; color: var(--navy); }
  .welcome { left: 216px; top: 846px; width: 515px; }
  .welcome p { margin-top: 13px; font-size: 8.4px; line-height: 12px; color: #555; }
  .welcome p + p { margin-top: 12px; }
  .inline-link { color: var(--orange); text-decoration: underline; }
  .testimonial { left: 757px; top: 846px; width: 255px; height: 160px; }
  .quote-mark { font-family: Georgia, serif; font-size: 30px; color: #d0d0d0; line-height: 1; }
  .quote-open { left: 4px; top: 30px; }
  .quote-close { left: 238px; top: 118px; }
  .quote-text { left: 25px; top: 51px; width: 210px; font-size: 9.7px; line-height: 16px; font-style: italic; color: var(--muted); }
  .quote-author { right: 0; top: 152px; font-size: 9.5px; color: var(--blue-btn); }

  .site-footer { left: 0; top: 1036px; width: 1200px; height: 85px; background: var(--navy-deep); color: var(--white); text-align: center; font-size: 8px; }
  .footer-links { margin-top: 42px; }
  .footer-links span { margin: 0 6px; }
  .copyright { margin-top: 5px; }
</style>
</head>
<body>
  <header class="site-header abs">
    <div class="brand abs">
      <div class="brand-name">MERIDALE EXCHANGE</div>
      <div class="brand-tagline">INTERNATIONAL MONEY TRANSFER</div>
    </div>
    <span class="social social-a abs" aria-label="Social link"></span>
    <span class="social social-b abs" aria-label="Social link"></span>
    <span class="social social-c abs" aria-label="Social link"></span>
  </header>

  <nav class="main-nav abs">
    <span class="nav-underline abs"></span>
    <span class="nav-item is-active abs" style="left:214px">Home</span>
    <span class="nav-item abs" style="left:288px">Services</span>
    <span class="nav-item abs" style="left:360px">Transfer</span>
    <span class="nav-item abs" style="left:435px">About us</span>
    <span class="nav-item abs" style="left:511px">Contact us</span>
    <span class="nav-item abs" style="left:592px">FAQ</span>
  </nav>

  <section class="hero abs">
    <h1 class="hero-title abs" style="font-weight:400">Transferring Money<br>Internationally?</h1>
    <p class="hero-sub abs">Transfer money over $10,000</p>
    <div class="btn-learn abs">Learn More</div>
    <div class="hero-art abs" role="img" aria-label="Illustration of rising blue 3D bar chart with red currency dice and an arrow trending upward"></div>
  </section>

  <section class="intro-strip abs">
    <span class="strip-brand abs">MERIDALE EXCHANGE</span>
    <p class="strip-text abs">Lorem ipsum dolor sit amet, consectetur adipisicing elit, sed do eiusmod tempor incididunt ut labore et dolore magna aliqua. Ut enim ad minim veniam, quis nostrud exercitation ullamco laboris nisi ut aliquip ex ea commodo consequat.</p>
    <div class="btn-strip abs">Lorum Ipsum</div>
  </section>

  <section class="features abs">
    <article class="card is-featured abs" style="left:12px">
      <div class="card-media abs"><span role="img" aria-label="Illustration of figures turning red gears" style="background:radial-gradient(circle,#e0463e 0%,#f2c7c4 55%,#fafafa 75%)"></span></div>
      <div class="card-body abs">
        <h3 class="card-title" style="font-weight:400">Solutions</h3>
        <p class="card-text">Lorem ipsum dolor sit amet, consectetur adipisicing elit, sed do eiusmod tempor incididunt ut labore et dolore magna</p>
      </div>
    </article>
    <article class="card abs" style="left:284px">
      <div class="card-media abs"><span role="img" aria-label="Illustration of a colourful bar chart with a magnifying glass" style="background:radial-gradient(circle,#e39a3a 0%,#9cc6e0 45%,#fafafa 75%)"></span></div>
      <div class="card-body abs">
        <h3 class="card-title" style="font-weight:400">Market Analysis</h3>
        <p class="card-text">Lorem ipsum dolor sit amet, consectetur adipisicing elit, sed do eiusmod tempor incididunt ut labore et dolore magna aliqua. Ut enim ad minim veniam, quis nostrud</p>
      </div>
    </article>
    <article class="card abs" style="left:553px">
      <div class="card-media abs"><span role="img" aria-label="Photo of a business team in dark suits" style="width:130px;background:linear-gradient(180deg,#d8c3b5 0%,#2b2b33 60%,#1c1c22 100%)"></span></div>
      <div class="card-body abs">
        <h3 class="card-title" style="font-weight:400">Corporate Value</h3>
        <p class="card-text">Lorem ipsum dolor sit amet, consectetur adipisicing elit, sed do eiusmod tempor incididunt ut labore et dolore magna aliqua. Ut enim ad minim veniam, quis nostrud</p>
      </div>
    </article>
  </section>

  <section class="welcome abs">
    <h2 class="section-title" style="font-weight:400">Welcome To Our Website</h2>
    <p>Lorem ipsum dolor sit amet, consectetur adipisicing elit, sed do eiusmod tempor incididunt ut labore et dolore magna aliqua. Ut enim ad minim veniam, quis nostrud exercitation ullamco laboris nisi ut aliquip ex ea commodo consequat. Duis aute irure dolor in reprehenderit in voluptate velit esse cillum dolore eu fugiat nulla pariatur. <span class="inline-link">Excepteur sint occaecat cupidatat non proident</span>, sunt in culpa qui officia deserunt mollit anim id est laborum.</p>
    <p>Lorem ipsum dolor sit amet, consectetur adipisicing elit, sed do eiusmod tempor incididunt ut labore et dolore magna aliqua. Ut enim ad minim veniam, quis nostrud exercitation ullamco laboris nisi ut aliquip ex ea commodo consequat. Duis aute irure dolor in reprehenderit in voluptate velit esse cillum dolore eu fugiat nulla pariatur. Excepteur sint occaecat cupidatat non proident, sunt in culpa qui officia deserunt mollit anim id est laborum.</p>
  </section>

  <aside class="testimonial abs">
    <h2 class="section-title" style="font-weight:400">Testimonial</h2>
    <span class="quote-mark quote-open abs">&ldquo;</span>
    <p class="quote-text abs">Lorem ipsum dolor sit amet, consectetur adipisicing elit, sed do eiusmod tempor incididunt ut labore et dolore magna aliqua. Ut enim ad minim veniam, quis nostrud exercitation ullamco laboris nisi ut aliquip.</p>
    <span class="quote-mark quote-close abs">&rdquo;</span>
    <span class="quote-author abs">- Admin</span>
  </aside>

  <footer class="site-footer abs">
    <div class="footer-links">Home<span>|</span>Services<span>|</span>Transfer<span>|</span>About us<span>|</span>Contact Us<span>|</span>FAQ</div>
    <div class="copyright">All Right Reserved 2013.</div>
  </footer>
</body>
</html>
```